We (R. T. Halvering & Associates, Inc.) are an executive Search firm based in Los Angeles that is exclusively focused in the Med Tech and Health Tech arenas.   I need a logo to communicate that we are a high end search firm, but also that we are focused in the medicine and science arenas called health tech and med tech.  Many of our clients have robotics and artificial intelligence type products, so it is very technology forward.  I tend to gravitate towards clean, sharp aesthetic as opposed to something that is really over the top.
Attached are files with my logo in two different layouts.  In addition to the letterhead and envelope, I also will need an electronic letterhead in Microsoft Word.  I tend to
I look forward to seeing the designs and just let me know if you have any questions.
Dale

```html
<!DOCTYPE html>
<html lang="en">
<head>
<meta charset="utf-8">
<title>R. T. Halvering &amp; Associates, Inc. — Stationery</title>
<link rel="stylesheet" href="https://fonts.googleapis.com/css2?family=Poppins:wght@400;600&family=Questrial&display=swap">
<style>
  :root {
    --backdrop: #7a7a7a;
    --paper: #f7f7f7;
    --paper-edge: #fbfbfb;
    --ink: #1b1b1b;
    --ink-soft: #555;
    --brand-blue: #4fa3dc;
    --signature-tone: #c9d9ec;
  }
  * { margin: 0; padding: 0; box-sizing: border-box; }
  html, body { width: 1200px; height: 877px; overflow: hidden; background: var(--backdrop); }
  .canvas { position: relative; width: 1200px; height: 877px; }

  .letterhead {
    position: absolute; left: 69px; top: 64px; width: 527px; height: 742px;
    background: linear-gradient(135deg, var(--paper-edge), var(--paper));
    box-shadow: 0 1px 3px rgba(0,0,0,.25);
  }
  .wordmark { position: absolute; display: flex; align-items: center; gap: 10px; }
  .wordmark__dot { width: 14px; height: 14px; border-radius: 50%; background: var(--brand-blue); }
  .wordmark__text { font-family: 'Poppins', sans-serif; font-weight: 600; color: var(--ink); line-height: 1.05; }
  .wordmark__name { display: block; letter-spacing: .2px; }
  .wordmark__sub { display: block; letter-spacing: 2.2px; }

  .letterhead .wordmark { left: 190px; top: 52px; }
  .letterhead .wordmark__name { font-size: 21px; }
  .letterhead .wordmark__sub { font-size: 9px; margin-top: 3px; }

  .letter-body { position: absolute; left: 45px; top: 206px; width: 438px; font-family: 'Questrial', sans-serif; color: var(--ink-soft); }
  .letter-body__salutation { font-size: 13.5px; color: #444; margin-bottom: 21px; }
  .letter-body p { font-size: 7.6px; line-height: 11.4px; text-align: justify; margin-bottom: 11.4px; }
  .letter-body__closing { position: absolute; left: 45px; top: 486px; font-family: 'Questrial', sans-serif; font-size: 7.6px; color: var(--ink-soft); }
  .signature { position: absolute; left: 42px; top: 526px; width: 94px; height: 32px; background: var(--signature-tone); border-radius: 3px; }

  .contact-strip { position: absolute; left: 0; top: 678px; width: 527px; height: 30px; font-family: 'Poppins', sans-serif; font-size: 8.6px; line-height: 9px; color: var(--ink); }
  .contact-item { position: absolute; top: 0; display: flex; align-items: center; gap: 6px; height: 24px; }
  .contact-item__icon { width: 18px; height: 18px; border-radius: 50%; background: var(--brand-blue); display: flex; align-items: center; justify-content: center; flex: none; }
  .contact-divider { position: absolute; top: 0; width: 1px; height: 24px; background: var(--brand-blue); }

  .envelope-back {
    position: absolute; left: 614px; top: 269px; width: 530px; height: 240px;
    background: linear-gradient(135deg, var(--paper-edge), var(--paper));
    box-shadow: 0 1px 3px rgba(0,0,0,.25);
  }
  .envelope-back__flap { position: absolute; left: 0; top: 0; }

  .envelope-front {
    position: absolute; left: 614px; top: 562px; width: 532px; height: 241px;
    background: linear-gradient(135deg, var(--paper-edge), var(--paper));
    box-shadow: 0 1px 3px rgba(0,0,0,.25);
  }
  .envelope-front .wordmark { left: 26px; top: 34px; }
  .envelope-front .wordmark__dot { width: 11px; height: 11px; }
  .envelope-front .wordmark__name { font-size: 15px; }
  .envelope-front .wordmark__sub { font-size: 6.6px; margin-top: 2px; letter-spacing: 1.7px; }
  .return-address { position: absolute; left: 72px; top: 69px; font-family: 'Poppins', sans-serif; font-size: 7px; line-height: 10px; color: #333; }
</style>
</head>
<body>
<main class="canvas">

  <section class="letterhead" aria-label="Letterhead">
    <div class="wordmark">
      <span class="wordmark__dot"></span>
      <span class="wordmark__text">
        <span class="wordmark__name">R. T. HALVERING</span>
        <span class="wordmark__sub">&amp; ASSOCIATES, INC.</span>
      </span>
    </div>

    <div class="letter-body">
      <div class="letter-body__salutation">Dear Mr. Calloway,</div>
      <p>Lorem ipsum dolor sit amet, consectetur adipiscing elit. Donec orci purus, luctus vitae dignissim eu, iaculis sed purus. Vivamus faucibus, ipsum nec aliquet viverra, leo mauris condimentum ligula, sit amet sagittis enim ligula quis arcu. Nam egestas tortor id nisi porttitor mattis. In tortor ante, ultricies in suscipit a, tempus non massa. Vivamus et auctor mi. Fusce vel massa nulla. Phasellus nec eros mauris, et scelerisque orci.</p>
      <p>Donec malesuada orci vitae nulla accumsan porta a id massa. Quisque accumsan iaculis magna sit amet fringilla. Maecenas consequat, magna eget tincidunt semper, odio nibh rutrum mi, id feugiat ante nisi eu risus. Vestibulum nunc orci, rhoncus a placerat in, ultricies in mi. Cras mattis varius eros, vel fringilla nisi suscipit eget. Quisque scelerisque sagittis nulla at porttitor.</p>
      <p>Sed id augue vitae urna euismod commodo aliquet a quam. Pellentesque arcu velit, cursus et malesuada ut, consequat et diam. Nullam erat sem, rhoncus id ullamcorper vitae, rhoncus et arcu. In ultricies ultricies nulla, ut rutrum nisi iaculis at. Donec eu magna a metus ornare faucibus. Fusce aliquet faucibus ultricies. Morbi semper, est id tincidunt gravida, sem arcu adipiscing lacus, ac bibendum nulla leo eu purus. Quisque nec diam sed risus consectetur a ccumsan quis quis nibh. Vestibulum id purus lorem.</p>
      <p>It is a long established fact that a reader will be distracted by the readable content of a page when looking at its layout. The point of using Lorem Ipsum is that it has a more-or-less normal distribution of letters, as opposed to using 'Content here, content here', making it look like readable English. Many desktop publishing packages</p>
    </div>
    <div class="letter-body__closing">Sincerely,</div>
    <div class="signature" role="img" aria-label="Handwritten signature of the sender"></div>

    <footer class="contact-strip">
      <div class="contact-item" style="left:40px">
        <span class="contact-item__icon">
          <svg width="10" height="10" viewBox="0 0 10 10" aria-hidden="true"><path d="M5 0.8a3 3 0 0 0-3 3c0 2.2 3 5.5 3 5.5s3-3.3 3-5.5a3 3 0 0 0-3-3z" fill="#fff"/><circle cx="5" cy="3.8" r="1.1" fill="#4fa3dc"/></svg>
        </span>
        <span>4219 Larkspur Court<br>Fairbrook, Oregon 97318</span>
      </div>
      <span class="contact-divider" style="left:193px"></span>
      <div class="contact-item" style="left:213px">
        <span class="contact-item__icon">
          <svg width="10" height="10" viewBox="0 0 10 10" aria-hidden="true"><path d="M2.2 1l1.6 0.1 0.7 2-1 0.8a6 6 0 0 0 2.6 2.6l0.8-1 2 0.7 0.1 1.6c0 .5-.6 1-1.2 1C4 8.8 1.2 6 1.2 2.2 1.2 1.6 1.7 1 2.2 1z" fill="#fff"/></svg>
        </span>
        <span>555-204-7391<br>555-318-6042</span>
      </div>
      <span class="contact-divider" style="left:324px"></span>
      <div class="contact-item" style="left:347px">
        <span class="contact-item__icon">
          <svg width="10" height="10" viewBox="0 0 10 10" aria-hidden="true"><circle cx="5" cy="5" r="3.8" fill="none" stroke="#fff" stroke-width="1"/><ellipse cx="5" cy="5" rx="1.6" ry="3.8" fill="none" stroke="#fff" stroke-width=".8"/><line x1="1.2" y1="5" x2="8.8" y2="5" stroke="#fff" stroke-width=".8"/></svg>
        </span>
        <span>info@rthalvering.com<br>www.rthalvering.com</span>
      </div>
    </footer>
  </section>

  <section class="envelope-back" aria-label="Envelope, back">
    <svg class="envelope-back__flap" width="530" height="74" viewBox="0 0 530 74" aria-hidden="true">
      <path d="M0 0H530L525 38Q521 74 488 74H42Q9 74 5 38Z" fill="#4fa3dc"/>
      <circle cx="269" cy="38" r="7" fill="#fff"/>
    </svg>
  </section>

  <section class="envelope-front" aria-label="Envelope, front">
    <div class="wordmark">
      <span class="wordmark__dot"></span>
      <span class="wordmark__text">
        <span class="wordmark__name">R. T. HALVERING</span>
        <span class="wordmark__sub">&amp; ASSOCIATES, INC.</span>
      </span>
    </div>
    <address class="return-address" style="font-style:normal">4219 Larkspur Court<br>Fairbrook, Oregon 97318</address>
  </section>

</main>
</body>
</html>
```